We are in search of a new business card design for our business. We have a Mexican Grocery Store called Tortilla Grove Market, we would like to see that some have mexican design, but we are open to any type of designs.

Phone: to be announced
Fax: to be announced

Address is:
2415 Calloway Blvd
Essex, MD 21221

```html
<!DOCTYPE html>
<html lang="en">
<head>
<meta charset="utf-8">
<title>Tortilla Grove Market – Business Card</title>
<link href="https://fonts.googleapis.com/css2?family=Open+Sans:wght@400;600;700;800&display=swap" rel="stylesheet">
<style>
  :root {
    --stage: #5b4b3f;
    --card-white: #ffffff;
    --brand-red: #a3212b;
    --brand-red-light: #d42525;
    --brand-red-dark: #98202a;
    --accent-orange: #f28c13;
    --accent-yellow: #ffc400;
    --accent-green: #2f7d12;
    --text-grey: #4a4a4a;
    --name-red: #8e1f2a;
  }
  * { box-sizing: border-box; margin: 0; padding: 0; }
  html, body {
    width: 1200px; height: 987px; overflow: hidden;
    background: var(--stage);
    font-family: "Open Sans", Arial, sans-serif;
  }
  .card {
    position: absolute; left: 293px; width: 615px; height: 352px;
    box-shadow: 0 4px 14px rgba(0,0,0,.35);
  }
  .card--front { top: 130px; background: var(--card-white); }
  .card--back {
    top: 506px;
    background: radial-gradient(ellipse at 45% 45%, var(--brand-red-light) 0%, #b7232a 45%, var(--brand-red-dark) 100%);
  }
  .brand-mark {
    position: absolute; display: flex; align-items: center; gap: 10px;
    font-weight: 800; line-height: 1.05; text-align: right;
  }
  .card--front .brand-mark { right: 30px; top: 52px; color: var(--brand-red); font-size: 27px; }
  .card--back .brand-mark { right: 24px; top: 252px; color: var(--card-white); font-size: 23px; }
  .brand-mark__dot { width: 16px; height: 16px; border-radius: 50%; background: currentColor; flex: none; }
  .person { position: absolute; left: 37px; top: 190px; }
  .person__name { color: var(--name-red); font-size: 22px; font-weight: 600; letter-spacing: .3px; }
  .person__title { color: var(--accent-orange); font-size: 16px; margin-top: 1px; }
  .divider { position: absolute; left: 37px; right: 29px; top: 250px; height: 1px; background: var(--name-red); }
  .contact { position: absolute; left: 41px; top: 262px; list-style: none; }
  .contact li { display: flex; align-items: center; gap: 6px; font-size: 16px; color: var(--text-grey); height: 25px; }
  .contact svg { width: 15px; height: 15px; fill: var(--name-red); }
  .address {
    position: absolute; right: 30px; top: 258px; text-align: right;
    font-size: 16px; color: var(--text-grey); line-height: 25px; font-style: normal;
  }
  .footer-band { position: absolute; left: 0; bottom: 0; width: 615px; height: 37px; }
  .website {
    position: absolute; right: 22px; bottom: 10px;
    color: var(--card-white); font-size: 16px; letter-spacing: 1px;
  }
</style>
</head>
<body>
  <section class="card card--front">
    <div class="brand-mark"><span class="brand-mark__dot"></span><span>Tortilla Grove<br>Market</span></div>

    <div class="person">
      <h1 class="person__name">DANIEL REYES</h1>
      <p class="person__title">CEO/FOUNDER</p>
    </div>
    <div class="divider"></div>

    <ul class="contact">
      <li>
        <svg viewBox="0 0 24 24" aria-hidden="true"><path d="M6.6 10.8a15 15 0 0 0 6.6 6.6l2.2-2.2c.3-.3.7-.4 1-.2 1.1.4 2.3.6 3.6.6.6 0 1 .4 1 1V20c0 .6-.4 1-1 1C10.6 21 3 13.4 3 4c0-.6.4-1 1-1h3.5c.6 0 1 .4 1 1 0 1.2.2 2.4.6 3.6.1.3 0 .7-.2 1z"/></svg>
        410 555 0182
      </li>
      <li>
        <svg viewBox="0 0 24 24" aria-hidden="true"><path d="M6 2h9l3 3v4H6zM3 10h18a1 1 0 0 1 1 1v7h-4v4H6v-4H2v-7a1 1 0 0 1 1-1zm5 7v3h8v-3z"/></svg>
        410 555 0193
      </li>
    </ul>

    <address class="address">2415 Calloway Blvd<br>Essex, MD 21221</address>

    <svg class="footer-band" viewBox="0 0 615 37" aria-hidden="true">
      <defs>
        <linearGradient id="stripe-orange" x1="0" x2="1" y1="0" y2="0">
          <stop offset="0" stop-color="var(--accent-orange)"/>
          <stop offset="1" stop-color="var(--accent-yellow)"/>
        </linearGradient>
      </defs>
      <polygon points="0,15 192,15 186,27 0,27" fill="url(#stripe-orange)"/>
      <polygon points="197,15 400,15 392,27 191,27" fill="var(--accent-green)"/>
      <polygon points="405,0 615,0 615,37 384,37" fill="var(--brand-red)"/>
      <rect x="0" y="27" width="615" height="10" fill="var(--brand-red)"/>
    </svg>
    <span class="website">www.tortillagrove.com</span>
  </section>

  <section class="card card--back">
    <div class="brand-mark"><span class="brand-mark__dot"></span><span>Tortilla Grove<br>Market</span></div>
  </section>
</body>
</html>
```